Room Hire at The Willowmere Wellbeing & Talking House to encourage therapists to hire rooms from us

An A4 page for magazine printing and use to send online as well.

We want to attract therapists to come and hire our beautiful rooms. We have a soft green, cream and brown colour theme and a professional, warm, elegant style (we hope)
I've uploaded the previous advert we had done through art bazaar which was aimed at attracting therapy clients.

Target Market(s)

psychotherapists and physical therapists searching to hire consulting rooms

Industry/Entity Type

Font styles to use
Serif
Sans Serif
Script
Other font styles liked:
• Good Vibes

Colors
cadf82
abd037
9bcb3c
fdf9ce
fff3d1

Requirements
Must have
• Please include this text
• Website address
• rooms@wmth-harbridge.example.co.uk address
• "The rooms are available to hire all day into the evenings and at weekends.
• There are 8 rooms, all suitable for Couples work, Individual Counselling or Supervision sessions. Some rooms are designed to be used by physical therapists as well. One of them is large enough to use for Family Therapy, to hold groups or to run Training Sessions for approximately fourteen people."
• The colour scheme to harmonise with our website theme colours and fonts - Colour RGA numbers
• Brown
• Red 65
• Green 53
• Blue 53
• Light green
• Red 129
• Green 157
• Blue 115
• www.wmth-harbridge.example.co.uk.
• Scrolling writing is Good Vibes by Plinko
• Be warm, calm, welcoming, professional styling, striking.
Nice to have
• Pictures of our rooms if we can provide enough quality for printing
Should not have
• Pictures of people touching each other.
• Not be too busy or angular

```html
<!DOCTYPE html>
<html lang="en">
<head>
<meta charset="utf-8">
<title>Willowmere Wellbeing &amp; Talking House – Room Hire Flyer</title>
<link href="https://fonts.googleapis.com/css2?family=Great+Vibes&family=Montserrat:wght@400;500;600;700&display=swap" rel="stylesheet">
<style>
  :root{
    --brown:#413535;
    --sage:#819d73;
    --olive:#9bb03c;
    --olive-text:#86992a;
    --cream:#f3eddd;
    --cream-light:#f8f4e8;
    --ink:#2b2424;
    --white:#ffffff;
    --backdrop:#e7e2d8;
  }
  *{box-sizing:border-box;margin:0;padding:0}
  html,body{width:1200px;height:1000px;overflow:hidden;background:var(--backdrop)}
  .canvas{position:relative;width:1200px;height:1000px}
  .flyer{position:absolute;left:250px;top:5px;width:700px;height:990px;background:var(--cream);overflow:hidden;box-shadow:0 4px 18px rgba(0,0,0,.18);font-family:"Montserrat",Arial,sans-serif}

  .hero{position:absolute;left:0;top:0;width:700px;height:300px}

  .logo-badge{position:absolute;left:35px;top:175px;width:180px;height:180px;border-radius:50%;background:var(--white);border:2px solid #c9c3bb;box-shadow:0 2px 6px rgba(0,0,0,.15);display:flex;flex-direction:column;align-items:center;justify-content:center;text-align:center;padding:0 22px;gap:9px;z-index:2}
  .logo-dot{width:22px;height:22px;border-radius:50%;background:var(--sage)}
  .logo-name{font-size:12px;font-weight:500;color:var(--ink);line-height:1.3}

  .intro{position:absolute;left:40px;top:368px;width:630px}
  .headline{font-family:"Great Vibes",cursive;font-weight:400;font-size:28px;line-height:34px;color:var(--ink);white-space:nowrap;margin-bottom:4px}
  .intro-text{font-size:13.5px;line-height:19px;color:var(--ink)}
  .intro-text strong{color:var(--sage);font-weight:700}

  .rooms-band{position:absolute;left:0;top:580px;width:700px;height:250px;background:var(--brown)}
  .rooms-band::after{content:"";position:absolute;left:0;right:0;bottom:0;height:5px;background:var(--olive)}

  .room-photo{position:absolute;width:175px;height:175px;border-radius:50%;border:8px solid var(--sage);z-index:1}
  .room-photo--armchair{left:40px;top:522px;background:radial-gradient(circle at 45% 40%,#8a5a4c,#6b4a3e 55%,#b8a48c)}
  .room-photo--session{left:265px;top:480px;background:radial-gradient(circle at 55% 40%,#c9c6c2,#8f8c8a 60%,#d9d4cc)}
  .room-photo--lounge{left:490px;top:458px;background:radial-gradient(circle at 50% 55%,#5a4a40,#a99a88 60%,#e3ddd0)}

  .rooms-title{position:absolute;left:250px;top:656px;font-family:"Great Vibes",cursive;font-weight:400;font-size:36px;line-height:44px;color:var(--white);z-index:1}
  .rooms-text{position:absolute;left:50px;top:712px;width:610px;font-size:13.5px;line-height:19px;color:var(--white);z-index:1}

  .footer{position:absolute;left:0;top:830px;width:700px;height:160px;background:var(--cream-light);display:flex;align-items:flex-start;padding:24px 30px 0 40px}
  .booking{width:285px;text-align:center}
  .booking-note{font-size:13px;font-weight:600;color:var(--olive-text);line-height:17px}
  .booking-phone{font-size:34px;font-weight:600;color:var(--ink);letter-spacing:.5px;margin-top:6px}
  .footer-divider{width:2px;height:100px;background:var(--ink);margin:2px 20px 0;flex:none}
  .contact{padding-top:2px}
  .contact-address{font-size:13px;font-weight:500;color:var(--olive-text);line-height:17px}
  .contact-web{font-size:14.5px;font-weight:700;color:var(--ink);margin-top:10px;white-space:nowrap}
  .contact-email{font-size:13px;font-weight:500;color:var(--ink);margin-top:6px;white-space:nowrap}
</style>
</head>
<body>
<div class="canvas">
  <article class="flyer">
    <svg class="hero" viewBox="0 0 700 300" role="img" aria-label="Photograph of a calm consulting room with a cream armchair, wooden sideboard and window">
      <defs>
        <linearGradient id="roomTone" x1="0" y1="0" x2="1" y2="1">
          <stop offset="0" stop-color="#d8c3a0"/>
          <stop offset=".55" stop-color="#eadcc0"/>
          <stop offset="1" stop-color="#c9b08a"/>
        </linearGradient>
      </defs>
      <path d="M0 0H700V195C620 235 500 262 380 262C250 262 120 235 0 198Z" fill="url(#roomTone)"/>
      <path d="M150 252C250 275 340 280 420 277C540 272 630 245 700 205" fill="none" stroke="var(--sage)" stroke-width="7"/>
    </svg>

    <div class="logo-badge">
      <span class="logo-dot"></span>
      <span class="logo-name">The Willowmere Wellbeing &amp; Talking House</span>
    </div>

    <section class="intro">
      <h1 class="headline">Confidential Therapeutic Services in the Heart of Millbrook</h1>
      <p class="intro-text">We have over <strong>30 carefully selected, qualified and professional therapists</strong> offering a range of services to help individuals, families and couples.</p>
    </section>

    <section class="rooms-band"></section>
    <div class="room-photo room-photo--armchair" role="img" aria-label="Photograph of a room with a leather armchair and patterned rug"></div>
    <div class="room-photo room-photo--session" role="img" aria-label="Photograph of a bright consulting room with a sofa"></div>
    <div class="room-photo room-photo--lounge" role="img" aria-label="Photograph of a group room with dark armchairs and a low table"></div>

    <h2 class="rooms-title">Our Discreet Rooms</h2>
    <p class="rooms-text">There are 8 rooms, all suitable for Couples work, Individual Counselling or Supervision sessions. Some rooms are designed to be used by physical therapists as well. One of them is large enough to use for Family Therapy, to hold groups or to run Training Sessions for approximately fourteen people.</p>

    <footer class="footer">
      <div class="booking">
        <p class="booking-note">The rooms are available to hire all day<br>into the evenings and at weekends</p>
        <p class="booking-phone">01632 960418</p>
      </div>
      <span class="footer-divider"></span>
      <div class="contact">
        <p class="contact-address">14 Orchard Lane, Millbrook,<br>Harbridge HB4 7QT</p>
        <p class="contact-web">www.wmth-harbridge.example.co.uk</p>
        <p class="contact-email">rooms@wmth-harbridge.example.co.uk</p>
      </div>
    </footer>
  </article>
</div>
</body>
</html>
```